Simple, Professional and neat business card design for Vendralo Inc.

We're looking to re-vamp our business card design. We're a supplier of innovative feed ingredients for the North American animal agriculture industry. We are located in Lucknow, Ontario, Canada and our flagship product is a product that prevents milk fever in dairy cows when the calve, it is fed before calving and is very effective compared to other alternatives available on the market today.

Our company has Danish roots and we import all of our product from our Danish partner/manufacturer in Denmark. We like our design to embrace high professionalism while remaining neat and simple.

Target Market(s)

B2B, Feed Mills, Veterinary Clinics, Large integrators/producers,

Industry/Entity Type

Agribusiness

Contact Information for Business Card

We like the rounded corners because they make the card easy to sit in a wallet and not many use it so it makes the card stand out, just possibly something to take account for during the design.

As you can also see on the sliders below, looking for a that simple but proffesional scandinavian design.

Requirements
Nice to have
• Rounded corners
Should not have
• Too vibrant

```html
<!DOCTYPE html>
<html lang="en">
<head>
<meta charset="utf-8">
<title>Vendralo Inc. – Business Card</title>
<link rel="stylesheet" href="https://fonts.googleapis.com/css2?family=Open+Sans:wght@400;600;700&display=swap">
<style>
  :root {
    --bg: #2b2e33;
    --card-white: #ffffff;
    --card-black: #141414;
    --brand-blue: #2f4fa2;
    --band-dark: #2a2a2a;
    --text-dark: #2a2a2a;
    --text-light: #d8d8d8;
  }
  * { margin: 0; padding: 0; box-sizing: border-box; }
  html, body {
    width: 1200px; height: 900px; overflow: hidden;
    background: var(--bg);
    font-family: "Open Sans", Arial, sans-serif;
  }
  .canvas { position: relative; width: 1200px; height: 900px; }

  .card {
    position: absolute; left: 280px;
    width: 640px; height: 366px;
    border-radius: 28px; overflow: hidden;
    box-shadow: 0 10px 30px rgba(0,0,0,0.35);
  }
  .card-front { top: 60px; background: var(--card-white); }
  .card-back  { top: 474px; background: var(--card-black); }

  /* front */
  .guide-line {
    position: absolute; left: 48px; top: 0; bottom: 40px;
    width: 2px; background: var(--brand-blue);
  }
  .holder-name {
    position: absolute; left: 70px; top: 44px;
    font-size: 24px; font-weight: 700; color: var(--brand-blue);
  }
  .holder-rule {
    position: absolute; left: 70px; top: 84px;
    width: 30px; height: 2px; background: var(--brand-blue);
  }
  .contact-list {
    position: absolute; left: 38px; top: 120px;
    list-style: none;
  }
  .contact-item {
    display: flex; align-items: center;
    height: 30px; font-size: 16px; color: var(--text-dark);
    white-space: nowrap;
  }
  .contact-icon {
    width: 22px; height: 22px; margin-right: 14px;
    background: var(--brand-blue); border-radius: 3px;
    display: flex; align-items: center; justify-content: center;
    flex-shrink: 0;
  }
  .contact-sep { margin: 0 12px; }

  .front-brand {
    position: absolute; right: 48px; top: 170px;
    width: 190px;
    display: flex; flex-direction: column; align-items: center; gap: 12px;
  }
  .brand-dot {
    width: 60px; height: 60px; border-radius: 50%;
    background: var(--brand-blue);
    flex-shrink: 0;
  }
  .brand-name {
    font-size: 20px; font-weight: 700; color: var(--brand-blue);
    text-transform: uppercase; white-space: nowrap;
  }

  .address-band {
    position: absolute; left: 0; right: 0; bottom: 0;
    height: 40px; background: var(--band-dark);
    display: flex; align-items: center;
  }
  .address-pin {
    width: 50px; height: 40px; background: var(--brand-blue);
    display: flex; align-items: center; justify-content: center;
  }
  .address-text {
    margin-left: 16px; font-size: 15px; color: var(--text-light);
  }

  /* back */
  .back-brand {
    position: absolute; left: 0; right: 0; top: 130px;
    display: flex; align-items: center; justify-content: center; gap: 16px;
  }
  .back-brand .brand-dot { width: 44px; height: 44px; }
  .back-brand .brand-name { font-size: 36px; }
  .back-web {
    position: absolute; left: 0; right: 0; top: 214px;
    text-align: center; font-size: 14px; letter-spacing: 4px;
    color: var(--text-light);
  }
</style>
</head>
<body>
<main class="canvas">

  <section class="card card-front">
    <div class="guide-line"></div>
    <h1 class="holder-name">Maren Holtvig</h1>
    <div class="holder-rule"></div>

    <ul class="contact-list">
      <li class="contact-item">
        <span class="contact-icon">
          <svg width="12" height="12" viewBox="0 0 12 12"><rect x="3" y="1" width="6" height="10" rx="1" fill="none" stroke="#fff" stroke-width="1.4"/></svg>
        </span>519-555-0142
      </li>
      <li class="contact-item">
        <span class="contact-icon">
          <svg width="12" height="12" viewBox="0 0 12 12"><path d="M2 2 L5 2 L6 4.5 L4.5 5.5 Q5.5 7.5 6.5 7.5 L7.5 6 L10 7 L10 10 Q4 10 2 2 Z" fill="#fff"/></svg>
        </span>519-555-0187<span class="contact-sep">I</span>888-555-0199(Toll free)
      </li>
      <li class="contact-item">
        <span class="contact-icon">
          <svg width="12" height="12" viewBox="0 0 12 12"><rect x="1.5" y="3" width="9" height="7" fill="none" stroke="#fff" stroke-width="1.4"/><rect x="3" y="1" width="6" height="3" fill="#fff"/></svg>
        </span>519-555-0163
      </li>
      <li class="contact-item">
        <span class="contact-icon">
          <svg width="12" height="12" viewBox="0 0 12 12"><rect x="1" y="2.5" width="10" height="7" fill="none" stroke="#fff" stroke-width="1.3"/><path d="M1 2.5 L6 6.5 L11 2.5" fill="none" stroke="#fff" stroke-width="1.3"/></svg>
        </span>maren@vendralo.com
      </li>
    </ul>

    <div class="front-brand">
      <span class="brand-dot"></span>
      <span class="brand-name">Vendralo Inc.</span>
    </div>

    <div class="address-band">
      <span class="address-pin">
        <svg width="14" height="18" viewBox="0 0 14 18"><path d="M7 1 C3.5 1 1.5 3.5 1.5 6.5 C1.5 10.5 7 17 7 17 C7 17 12.5 10.5 12.5 6.5 C12.5 3.5 10.5 1 7 1 Z" fill="#f0d890"/><circle cx="7" cy="6.5" r="2.2" fill="#2f4fa2"/></svg>
      </span>
      <span class="address-text">Box 472, Brenton, Ontario Canada N0G3K1</span>
    </div>
  </section>

  <section class="card card-back">
    <div class="back-brand">
      <span class="brand-dot"></span>
      <span class="brand-name">Vendralo Inc.</span>
    </div>
    <p class="back-web">www.vendralo.com</p>
  </section>

</main>
</body>
</html>
```